Save the Date - An Evening to Celebrate

We would like to send out a "save the date" announcement for our upcoming employee appreciation banquet. The purpose of our banquet is to recoqnize our employees and business partners. The theme will be casino. I've attached a sample with the pertinent information. The idea is to generate enthusiasm for the upcoming event.

Target Market(s)

Employees and business partners

Industry/Entity Type

Automotive

Font styles to use
Serif

Requirements
Must have
• Logo

```html
<!DOCTYPE html>
<html lang="en">
<head>
<meta charset="utf-8">
<title>Save the Date – An Evening to Celebrate</title>
<link rel="stylesheet" href="https://fonts.googleapis.com/css2?family=Orbitron:wght@600;700&family=Gelasio:wght@400&family=Arimo:wght@400;700&display=swap">
<style>
  :root {
    --page-black: #050505;
    --vignette-grey: #3a3a3c;
    --panel-dark: #4a4a4c;
    --panel-light: #6e6e70;
    --frame-black: #0b0b0b;
    --emblem-tone: #c9c9cb;
    --accent-red: #ad1f2d;
    --ink: #111111;
    --white: #ffffff;
  }
  * { margin: 0; padding: 0; box-sizing: border-box; }
  html, body {
    width: 999px; height: 1200px; overflow: hidden;
    background: var(--page-black);
  }
  .canvas {
    position: relative; width: 999px; height: 1200px; overflow: hidden;
    background: radial-gradient(ellipse at 50% 50%, var(--vignette-grey) 0%, #1c1c1d 60%, var(--page-black) 100%);
  }
  .panel {
    position: absolute; left: 107px; top: 50px; width: 786px; height: 1098px;
    border: 1px solid #8a8a8c;
    background:
      repeating-linear-gradient(165deg, rgba(255,255,255,0.07) 0 22px, rgba(0,0,0,0.06) 22px 60px),
      linear-gradient(160deg, var(--panel-light), var(--panel-dark) 55%, var(--panel-light));
  }
  .ticket { position: absolute; left: 0; top: 0; }
  .emblem {
    position: absolute; left: 394px; top: 157px; width: 210px; height: 210px;
    border-radius: 50%;
    background: radial-gradient(circle, var(--emblem-tone) 0%, rgba(201,201,203,0.6) 60%, rgba(201,201,203,0) 72%);
  }
  .headline, .title {
    position: absolute; left: 0; width: 999px; text-align: center;
    font-family: "Orbitron", sans-serif; font-weight: 700; color: var(--accent-red);
  }
  .headline { top: 224px; font-size: 57px; line-height: 80px; }
  .invite-banner { position: absolute; left: 271px; top: 381px; }
  .invite-text {
    position: absolute; left: 271px; top: 381px; width: 458px; height: 78px;
    display: flex; align-items: center; justify-content: center;
    font-family: "Gelasio", serif; font-size: 43px; color: var(--white);
  }
  .title { top: 505px; font-size: 64px; font-weight: 600; line-height: 88px; }
  .divider {
    position: absolute; left: 288px; width: 424px; height: 3px;
    background: var(--ink);
  }
  .values {
    position: absolute; left: 0; top: 728px; width: 999px; list-style: none; text-align: center;
    font-family: "Arimo", sans-serif; font-weight: 700; font-size: 38px; color: var(--ink);
  }
  .values li { height: 63px; line-height: 48px; }
  .details {
    position: absolute; left: 0; top: 955px; width: 999px; text-align: center;
    font-family: "Arimo", sans-serif; font-size: 32px; line-height: 42px; color: var(--ink);
  }
</style>
</head>
<body>
<main class="canvas">
  <div class="panel"></div>

  <svg class="ticket" width="999" height="1200" viewBox="0 0 999 1200" aria-hidden="true">
    <defs>
      <linearGradient id="cardFill" x1="0" y1="0" x2="1" y2="1">
        <stop offset="0" stop-color="#dcdcdd"/>
        <stop offset="0.5" stop-color="#ededee"/>
        <stop offset="1" stop-color="#d4d4d6"/>
      </linearGradient>
    </defs>
    <path fill="var(--frame-black)" d="M234 106 H766 A62 62 0 0 0 828 168 V1033 A62 62 0 0 0 766 1095 H234 A62 62 0 0 0 172 1033 V168 A62 62 0 0 0 234 106 Z"/>
    <path fill="url(#cardFill)" d="M234 122 H766 A46 46 0 0 0 812 168 V1033 A46 46 0 0 0 766 1079 H234 A46 46 0 0 0 188 1033 V168 A46 46 0 0 0 234 122 Z"/>
  </svg>

  <div class="emblem" role="img" aria-label="Company emblem behind the headline"></div>
  <h1 class="headline">Save the date</h1>

  <svg class="invite-banner" width="458" height="78" viewBox="0 0 458 78" aria-hidden="true">
    <path fill="var(--frame-black)" d="M14 0 H444 A14 14 0 0 0 458 14 V64 A14 14 0 0 0 444 78 H14 A14 14 0 0 0 0 64 V14 A14 14 0 0 0 14 0 Z"/>
  </svg>
  <p class="invite-text">Invites You to Attend</p>

  <h2 class="title">"An Evening to<br>Celebrate"</h2>

  <div class="divider" style="top:707px"></div>

  <ul class="values">
    <li>Our People</li>
    <li>Our Community</li>
    <li>Our Company</li>
  </ul>

  <div class="divider" style="top:930px"></div>

  <p class="details">Saturday, May 13th, 2017<br>at the Harbourview Hotel Vancouver</p>
</main>
</body>
</html>
```